Email Signature

Hello,

We need an editable file so that when new staff start or someone is promoted we can easily edit this file.

The previous designer has not kept the email signatures uniform they should all be as per Colin Tresk signature.

I also need the Farid Noori changes as below -
Senior Mechanical Engineer
Email should be farid.noori@veltonix.com.au

You can see the Glen Harwick file is different I need this the same as Colin Tresk format but with details changed.

Also need a new one with details as per below -
Derek Pluim
Commercial Manager
0417 305 162
derek.pluim@veltonix.com.au
www.veltonix.com.au

```html
<!DOCTYPE html>
<html lang="en">
<head>
<meta charset="utf-8">
<title>Veltonix Email Signatures</title>
<link rel="stylesheet" href="https://fonts.googleapis.com/css2?family=Kanit:wght@400;500;600&display=swap">
<style>
  :root{
    --backdrop:#5b5b5b;
    --card:#ffffff;
    --name-blue:#1a8fd6;
    --icon-blue:#1e8fd5;
    --band-blue:#1b94d6;
    --band-green:#b3d657;
    --brand-cyan:#00c3f5;
    --tag-grey:#606164;
    --ink:#1b1b1b;
  }
  *{margin:0;padding:0;box-sizing:border-box}
  html,body{width:858px;height:1200px;overflow:hidden;background:var(--backdrop)}
  body{position:relative;font-family:"Kanit",sans-serif;color:var(--ink)}
  .signature{position:absolute;left:19px;width:823px;height:273px;background:var(--card);overflow:hidden}
  .signature--1{top:19px}
  .signature--2{top:316px}
  .signature--3{top:612px}
  .signature--4{top:908px}

  .staff-name{position:absolute;left:32px;top:24px;font-size:33px;font-weight:600;color:var(--name-blue);line-height:1;letter-spacing:.3px}
  .staff-role{position:absolute;left:33px;top:68px;font-size:19px;font-weight:400;line-height:1}
  .contact-list{position:absolute;left:32px;top:108px;list-style:none}
  .contact-item{display:flex;align-items:center;height:30px;margin-bottom:8px;font-size:20px;line-height:1}
  .contact-icon{width:30px;height:30px;border-radius:50%;background:var(--icon-blue);display:flex;align-items:center;justify-content:center;margin-right:9px;flex:none}
  .contact-icon svg{width:17px;height:17px}

  .brand{position:absolute;left:418px;top:22px;width:376px;text-align:center}
  .brand-name{font-size:70px;font-weight:600;color:var(--brand-cyan);line-height:1.3;letter-spacing:1px}
  .brand-tagline{font-size:24.5px;font-weight:400;color:var(--tag-grey);line-height:1;margin-top:14px;white-space:nowrap}
  .brand-division{display:flex;align-items:center;gap:10px;margin-top:5px;font-size:18px;color:var(--brand-cyan);line-height:1;white-space:nowrap}
  .brand-division::before,.brand-division::after{content:"";flex:1;height:2px;background:var(--brand-cyan)}

  .footer-band{position:absolute;left:0;bottom:0;width:823px;height:46px}
  .footer-band svg.band-shape{position:absolute;inset:0}
  .footer-address{position:absolute;left:42px;top:12px;display:flex;align-items:center;gap:8px;color:#fff;font-size:19px;font-weight:500;line-height:1}
  .footer-address svg{width:15px;height:20px}
  .footer-phone{position:absolute;left:564px;top:15px;font-size:19px;font-weight:500;line-height:1;color:var(--ink)}
  .social-list{position:absolute;left:714px;top:14px;display:flex;gap:6px;list-style:none}
  .social-dot{width:23px;height:23px;border-radius:50%;background:var(--icon-blue)}
</style>
</head>
<body>

<svg width="0" height="0" style="position:absolute">
  <defs>
    <symbol id="icon-phone" viewBox="0 0 24 24"><path d="M6.6 3.5l2.6 0 1.2 4-2 1.6c1 2.2 2.7 3.9 4.9 4.9l1.6-2 4 1.2 0 2.6c0 1-1 1.7-2 1.6C10.6 16.9 7.1 13.4 5 7.1c-.3-1 .5-3.6 1.6-3.6z" fill="none" stroke="#fff" stroke-width="1.7" stroke-linejoin="round"/></symbol>
    <symbol id="icon-mail" viewBox="0 0 24 24"><rect x="3" y="6" width="18" height="12" rx="1.5" fill="none" stroke="#fff" stroke-width="1.7"/><path d="M3.5 7l8.5 6.5L20.5 7" fill="none" stroke="#fff" stroke-width="1.7"/></symbol>
    <symbol id="icon-web" viewBox="0 0 24 24"><g fill="none" stroke="#fff" stroke-width="1.5"><circle cx="12" cy="12" r="8.5"/><ellipse cx="12" cy="12" rx="3.8" ry="8.5"/><path d="M3.5 12h17M5 7.5h14M5 16.5h14"/></g></symbol>
    <symbol id="icon-pin" viewBox="0 0 15 20"><path d="M7.5 0C3.4 0 0 3.2 0 7.3 0 12.5 7.5 20 7.5 20S15 12.5 15 7.3C15 3.2 11.6 0 7.5 0zm0 10.2a3 3 0 110-6 3 3 0 010 6z" fill="#fff"/></symbol>
    <symbol id="band" viewBox="0 0 823 46"><polygon points="0,0 695,0 695,2.5 565,2.5 522,46 0,46" fill="var(--band-blue)"/><polygon points="572,6 823,6 823,46 531,46" fill="var(--band-green)"/></symbol>
  </defs>
</svg>

<section class="signature signature--1">
  <h1 class="staff-name">Colin Tresk</h1>
  <p class="staff-role">Site Project Manager</p>
  <ul class="contact-list">
    <li class="contact-item"><span class="contact-icon"><svg><use href="#icon-phone"/></svg></span>0452 813 660</li>
    <li class="contact-item"><span class="contact-icon"><svg><use href="#icon-mail"/></svg></span>colin.tresk@veltonix.com.au</li>
    <li class="contact-item"><span class="contact-icon"><svg><use href="#icon-web"/></svg></span>www.veltonix.com.au</li>
  </ul>
  <div class="brand">
    <div class="brand-name">VELTONIX</div>
    <div class="brand-tagline">Commercial Air Conditioning</div>
    <div class="brand-division">A Division of Harwick Air</div>
  </div>
  <footer class="footer-band">
    <svg class="band-shape" width="823" height="46"><use href="#band"/></svg>
    <div class="footer-address"><svg><use href="#icon-pin"/></svg>14/220 Marlow Road, Kedron QLD 4031</div>
    <div class="footer-phone">1300 462 918</div>
    <ul class="social-list" aria-label="Social links"><li class="social-dot"></li><li class="social-dot"></li><li class="social-dot"></li></ul>
  </footer>
</section>

<section class="signature signature--2">
  <h1 class="staff-name">Glen Harwick</h1>
  <p class="staff-role">Director</p>
  <ul class="contact-list">
    <li class="contact-item"><span class="contact-icon"><svg><use href="#icon-phone"/></svg></span>0438 917 204</li>
    <li class="contact-item"><span class="contact-icon"><svg><use href="#icon-mail"/></svg></span>glen.harwick@veltonix.com.au</li>
    <li class="contact-item"><span class="contact-icon"><svg><use href="#icon-web"/></svg></span>www.veltonix.com.au</li>
  </ul>
  <div class="brand">
    <div class="brand-name">VELTONIX</div>
    <div class="brand-tagline">Commercial Air Conditioning</div>
    <div class="brand-division">A Division of Harwick Air</div>
  </div>
  <footer class="footer-band">
    <svg class="band-shape" width="823" height="46"><use href="#band"/></svg>
    <div class="footer-address"><svg><use href="#icon-pin"/></svg>14/220 Marlow Road, Kedron QLD 4031</div>
    <div class="footer-phone">1300 462 918</div>
    <ul class="social-list" aria-label="Social links"><li class="social-dot"></li><li class="social-dot"></li><li class="social-dot"></li></ul>
  </footer>
</section>

<section class="signature signature--3">
  <h1 class="staff-name">Farid Noori</h1>
  <p class="staff-role">Senior Mechanical Engineer</p>
  <ul class="contact-list">
    <li class="contact-item"><span class="contact-icon"><svg><use href="#icon-phone"/></svg></span>0421 586 073</li>
    <li class="contact-item"><span class="contact-icon"><svg><use href="#icon-mail"/></svg></span>farid.noori@veltonix.com.au</li>
    <li class="contact-item"><span class="contact-icon"><svg><use href="#icon-web"/></svg></span>www.veltonix.com.au</li>
  </ul>
  <div class="brand">
    <div class="brand-name">VELTONIX</div>
    <div class="brand-tagline">Commercial Air Conditioning</div>
    <div class="brand-division">A Division of Harwick Air</div>
  </div>
  <footer class="footer-band">
    <svg class="band-shape" width="823" height="46"><use href="#band"/></svg>
    <div class="footer-address"><svg><use href="#icon-pin"/></svg>14/220 Marlow Road, Kedron QLD 4031</div>
    <div class="footer-phone">1300 462 918</div>
    <ul class="social-list" aria-label="Social links"><li class="social-dot"></li><li class="social-dot"></li><li class="social-dot"></li></ul>
  </footer>
</section>

<section class="signature signature--4">
  <h1 class="staff-name">Derek Pluim</h1>
  <p class="staff-role">Commercial Manager</p>
  <ul class="contact-list">
    <li class="contact-item"><span class="contact-icon"><svg><use href="#icon-phone"/></svg></span>0417 305 162</li>
    <li class="contact-item"><span class="contact-icon"><svg><use href="#icon-mail"/></svg></span>derek.pluim@veltonix.com.au</li>
    <li class="contact-item"><span class="contact-icon"><svg><use href="#icon-web"/></svg></span>www.veltonix.com.au</li>
  </ul>
  <div class="brand">
    <div class="brand-name">VELTONIX</div>
    <div class="brand-tagline">Commercial Air Conditioning</div>
    <div class="brand-division">A Division of Harwick Air</div>
  </div>
  <footer class="footer-band">
    <svg class="band-shape" width="823" height="46"><use href="#band"/></svg>
    <div class="footer-address"><svg><use href="#icon-pin"/></svg>14/220 Marlow Road, Kedron QLD 4031</div>
    <div class="footer-phone">1300 462 918</div>
    <ul class="social-list" aria-label="Social links"><li class="social-dot"></li><li class="social-dot"></li><li class="social-dot"></li></ul>
  </footer>
</section>

</body>
</html>
```